Business Cards for a law firm

Business cards for our law firm. Use our silhoette logo and OAK HARBOR - check our website (www.oakharbor-legal.com)

Contact Information for Business Card

our silhouette logo, OAK HARBOR, 800-555-0147, Dorian Kestrup, dorian@oakharbor-legal.com

Requirements
Must have
• our silhouette logo, OAK HARBOR, 800-555-0147, Dorian Kestrup, dorian@oakharbor-legal.com

```html
<!DOCTYPE html>
<html lang="en">
<head>
<meta charset="utf-8">
<title>Oak Harbor Business Cards</title>
<link rel="stylesheet" href="https://fonts.googleapis.com/css2?family=Cinzel:wght@600&family=Lato:wght@400;700&display=swap">
<style>
  :root {
    --page: #e7e6e7;
    --navy: #1a336c;
    --navy-soft: #22428a;
    --navy-mid: #2a4c94;
    --white: #ffffff;
    --ink: #1b1b1b;
    --figure-light: #eef0f5;
    --figure-tint: #c9d0e2;
  }
  * { margin: 0; padding: 0; box-sizing: border-box; }
  html, body { width: 1200px; height: 1108px; overflow: hidden; }
  body { background: var(--page); position: relative; font-family: "Lato", sans-serif; }

  .card { position: absolute; width: 770px; height: 442px; overflow: hidden; }
  .card-front { left: 231px; top: 68px; background: var(--white); box-shadow: 0 12px 22px rgba(0,0,0,.18); }
  .card-back { left: 241px; top: 590px; background: var(--navy); box-shadow: 0 12px 22px rgba(0,0,0,.22); }

  .emblem-area { position: absolute; border-radius: 60px 60px 0 0; }
  .card-front .emblem-area {
    left: 26px; top: 68px; width: 248px; height: 356px;
    background: linear-gradient(180deg, var(--navy-mid) 0%, var(--navy) 70%);
  }
  .card-back .emblem-main {
    left: 6px; top: 4px; width: 286px; height: 434px;
    background: linear-gradient(180deg, var(--white) 0%, var(--figure-light) 55%, var(--figure-tint) 100%);
  }
  .card-back .emblem-faint {
    left: 484px; top: 8px; width: 282px; height: 434px;
    background: linear-gradient(180deg, var(--navy-soft) 0%, var(--navy) 100%);
    opacity: .6;
  }

  .base-band { position: absolute; left: 0; bottom: 0; width: 100%; height: 20px; background: var(--navy); }

  .firm-name {
    position: absolute; font-family: "Cinzel", serif; font-weight: 600;
    white-space: nowrap; line-height: 1;
  }
  .card-front .firm-name { right: 47px; top: 44px; font-size: 42px; letter-spacing: 7px; color: var(--navy); }
  .card-back .firm-name { right: 38px; top: 372px; font-size: 40px; letter-spacing: 6px; color: var(--white); }

  .person { position: absolute; right: 47px; top: 178px; text-align: right; }
  .person-name { font-size: 28px; font-weight: 700; color: var(--navy); line-height: 1.2; }
  .person-role { font-size: 20px; color: var(--ink); margin-top: 6px; }

  .contacts { position: absolute; right: 47px; top: 278px; list-style: none; }
  .contacts li {
    display: flex; justify-content: flex-end; align-items: center; gap: 12px;
    font-size: 20px; color: var(--ink); height: 34px;
  }
  .contacts svg { width: 22px; height: 22px; flex: none; }
</style>
</head>
<body>
  <section class="card card-front">
    <div class="emblem-area" role="img" aria-label="Firm silhouette emblem of two standing figures"></div>
    <div class="firm-name">OAK HARBOR</div>
    <div class="person">
      <div class="person-name">Dorian Kestrup</div>
      <div class="person-role">Attorney</div>
    </div>
    <ul class="contacts">
      <li>800-555-0147
        <svg viewBox="0 0 24 24"><path fill="var(--navy)" d="M6.6 10.8a15 15 0 0 0 6.6 6.6l2.2-2.2c.3-.3.7-.4 1-.2 1.1.4 2.3.6 3.6.6.6 0 1 .4 1 1V20c0 .6-.4 1-1 1A17 17 0 0 1 3 4c0-.6.4-1 1-1h3.5c.6 0 1 .4 1 1 0 1.3.2 2.5.6 3.6.1.3 0 .7-.2 1z"/></svg></li>
      <li>dorian@oakharbor-legal.com
        <svg viewBox="0 0 24 24"><rect x="1" y="5" width="22" height="14" fill="var(--navy)"/><path d="M2 6l10 7 10-7" fill="none" stroke="var(--white)" stroke-width="1.8"/></svg></li>
      <li>www.oakharbor-legal.com
        <svg viewBox="0 0 24 24"><circle cx="12" cy="12" r="10.5" fill="var(--navy)"/><path d="M8 5c2 1 3 3 1 4.5s-1 3 1 4-1 4-2 5M15 4.5c-1 2 1 3.5 3.5 3.5M14 14c2 0 3 2 2 4.5" fill="none" stroke="var(--white)" stroke-width="1.6"/></svg></li>
    </ul>
    <div class="base-band"></div>
  </section>

  <section class="card card-back">
    <div class="emblem-area emblem-main" role="img" aria-label="Firm silhouette emblem of two standing figures in white"></div>
    <div class="emblem-area emblem-faint" role="img" aria-label="Faint repeat of the silhouette emblem"></div>
    <div class="firm-name">OAK HARBOR</div>
  </section>
</body>
</html>
```